KORBALT

The business want a professional looking business card. We have a scetch we will add but want the extra upgrade, and would like more suggestions for variations of our business cards.

```html
<!DOCTYPE html>
<html lang="en">
<head>
<meta charset="utf-8">
<title>KORBALT – Business Cards</title>
<link href="https://fonts.googleapis.com/css2?family=Marcellus&family=Montserrat:wght@400;500&display=swap" rel="stylesheet">
<style>
  :root {
    --backdrop: #e6dccf;
    --ivory: #f3efe6;
    --ink: #151515;
    --black-card: #1b1b1b;
    --gold: #b48a45;
    --gold-light: #c9a35c;
    --sand: #e4d8c2;
    --white: #f4f1ea;
  }
  * { margin: 0; padding: 0; box-sizing: border-box; }
  html, body { width: 1200px; height: 800px; overflow: hidden; }
  body {
    background: var(--backdrop);
    font-family: "Montserrat", sans-serif;
    position: relative;
  }
  .card {
    position: absolute;
    width: 500px;
    height: 286px;
    border-radius: 3px;
    box-shadow: 0 10px 24px rgba(80, 60, 40, 0.18);
    overflow: hidden;
  }
  .card--ivory { background: var(--ivory); color: var(--ink); }
  .card--black { background: var(--black-card); color: var(--white); }
  .front-ivory { left: 70px; top: 90px; }
  .front-black { left: 630px; top: 90px; }
  .back-ivory { left: 70px; top: 424px; }
  .back-black { left: 630px; top: 424px; }

  .company {
    font-family: "Marcellus", serif;
    font-size: 25px;
    letter-spacing: 2.5px;
    line-height: 1.2;
  }
  .person { font-size: 16px; margin-top: 8px; letter-spacing: 0.3px; }
  .role { font-size: 13px; color: var(--gold-light); margin-top: 4px; letter-spacing: 0.5px; }

  .front-ivory .content { position: absolute; left: 44px; top: 40px; }
  .front-black .content { position: absolute; left: 44px; top: 34px; }

  .corner-name {
    position: absolute;
    right: 32px;
    top: 28px;
    font-family: "Marcellus", serif;
    font-size: 13px;
    letter-spacing: 2px;
    color: var(--gold);
  }
  .accent-rule {
    position: absolute;
    right: 58px;
    top: 116px;
    width: 40px;
    height: 2px;
    background: var(--gold-light);
  }

  .contacts {
    position: absolute;
    left: 44px;
    list-style: none;
    font-size: 14px;
    letter-spacing: 0.6px;
  }
  .front-ivory .contacts { top: 176px; }
  .front-black .contacts { top: 180px; }
  .contacts li { display: flex; align-items: center; gap: 14px; height: 24px; }
  .contacts svg { width: 18px; height: 18px; flex: none; }

  .back-brand {
    font-family: "Marcellus", serif;
    font-size: 30px;
    letter-spacing: 5px;
  }
  .since {
    font-size: 11px;
    letter-spacing: 5px;
    color: var(--gold);
    margin-top: 6px;
  }
  .back-ivory .brand-block { position: absolute; left: 44px; bottom: 46px; }
  .back-ivory .watermark-name {
    position: absolute;
    right: -30px;
    top: 60px;
    font-family: "Marcellus", serif;
    font-size: 92px;
    letter-spacing: 4px;
    color: var(--sand);
    transform: rotate(-90deg) translateX(-40%);
    transform-origin: right top;
    white-space: nowrap;
  }
  .back-black .brand-block {
    position: absolute;
    inset: 0;
    display: flex;
    flex-direction: column;
    align-items: center;
    justify-content: center;
    text-align: center;
  }
  .brand-dot {
    width: 46px;
    height: 46px;
    border-radius: 50%;
    background: var(--gold-light);
    margin-bottom: 22px;
  }
  .back-black .since { color: var(--gold-light); }
</style>
</head>
<body>

  <!-- Front, ivory -->
  <section class="card card--ivory front-ivory">
    <span class="corner-name">KORBALT</span>
    <div class="content">
      <h1 class="company">KORBALT ARNESTAD</h1>
      <p class="person">Lars Erik Arnestad</p>
      <p class="role">CEO &amp; Founder</p>
    </div>
    <ul class="contacts">
      <li>
        <svg viewBox="0 0 24 24" fill="none" stroke="#b48a45" stroke-width="1.6"><path d="M5 3h4l2 5-2.5 1.5a11 11 0 0 0 6 6L16 13l5 2v4a2 2 0 0 1-2 2A17 17 0 0 1 3 5a2 2 0 0 1 2-2z"/></svg>
        004791234567
      </li>
      <li>
        <svg viewBox="0 0 24 24" fill="none" stroke="#b48a45" stroke-width="1.6"><rect x="3" y="5" width="18" height="14"/><path d="M3 6l9 7 9-7"/></svg>
        korbalt.llc@mailbox.com
      </li>
      <li>
        <svg viewBox="0 0 24 24" fill="none" stroke="#b48a45" stroke-width="1.6"><circle cx="12" cy="12" r="9"/><path d="M3 12h18M12 3c3 3 3 15 0 18M12 3c-3 3-3 15 0 18"/></svg>
        www.korbalt.llc
      </li>
    </ul>
  </section>

  <!-- Front, black -->
  <section class="card card--black front-black">
    <div class="content">
      <h1 class="company">KORBALT<br>ARNESTAD</h1>
      <p class="person">Lars Erik Arnestad</p>
      <p class="role">CEO &amp; Founder</p>
    </div>
    <span class="accent-rule"></span>
    <ul class="contacts">
      <li>
        <svg viewBox="0 0 24 24" fill="none" stroke="#c9a35c" stroke-width="1.6"><path d="M5 3h4l2 5-2.5 1.5a11 11 0 0 0 6 6L16 13l5 2v4a2 2 0 0 1-2 2A17 17 0 0 1 3 5a2 2 0 0 1 2-2z"/></svg>
        004791234567
      </li>
      <li>
        <svg viewBox="0 0 24 24" fill="none" stroke="#c9a35c" stroke-width="1.6"><rect x="3" y="5" width="18" height="14"/><path d="M3 6l9 7 9-7"/></svg>
        korbalt.llc@mailbox.com
      </li>
      <li>
        <svg viewBox="0 0 24 24" fill="none" stroke="#c9a35c" stroke-width="1.6"><circle cx="12" cy="12" r="9"/><path d="M3 12h18M12 3c3 3 3 15 0 18M12 3c-3 3-3 15 0 18"/></svg>
        www.korbalt.llc
      </li>
    </ul>
  </section>

  <!-- Back, ivory -->
  <section class="card card--ivory back-ivory">
    <span class="watermark-name" aria-hidden="true">KORBALT</span>
    <div class="brand-block">
      <p class="back-brand">KORBALT</p>
      <p class="since">SINCE 2026</p>
    </div>
  </section>

  <!-- Back, black -->
  <section class="card card--black back-black">
    <div class="brand-block">
      <span class="brand-dot"></span>
      <p class="back-brand">KORBALT</p>
      <p class="since">SINCE 2026</p>
    </div>
  </section>

</body>
</html>
```